Website Refresh for Niche Pet Website

We have a site that needs a fresh, modern look. This site gets approx 500K views a month and we want a re-design.

Category layout
New blog template layout

We need to keep the large rolling ads on the home page
The small ad need to be placed on the side when looking at the interior page.

We need a modern slick easy to use site

Target Market(s)

Breeders and pet buyers in the UK

Industry/Entity Type

pets

Number of Pages Required

4 page

Requirements
Must have
• Be Gun Dog specific - these are for working homes. Creative way to showcase the ads, breeds etc.
Nice to have
• We are open to logo improvements and colour, however, this is the UK market for buying and selling gun dogs. The grren and gold do work well.

```html
<!DOCTYPE html>
<html lang="en">
<head>
<meta charset="utf-8">
<title>FieldHound Market – Find Your Perfect Gundog</title>
<link href="https://fonts.googleapis.com/css2?family=Roboto:wght@400;500;700&display=swap" rel="stylesheet">
<style>
:root{
  --gold:#d6a45a;
  --gold-dark:#c48f3e;
  --green:#4f6135;
  --green-dark:#2d3a1c;
  --grey-band:#ececec;
  --panel:#f3f3f3;
  --text:#3a3a3a;
  --white:#ffffff;
}
*{box-sizing:border-box;margin:0;padding:0}
html,body{width:1200px;height:4264px;overflow:hidden}
body{font-family:'Roboto',sans-serif;color:var(--text);background:var(--white);position:relative}

/* top nav */
.topbar{position:absolute;left:0;top:0;width:1200px;height:60px;background:var(--gold);border-bottom:3px solid var(--green-dark);z-index:2}
.menu-btn{position:absolute;left:158px;top:17px;width:34px;height:26px;border:2px solid #fff;border-radius:6px}
.menu-btn i{position:absolute;left:6px;width:18px;height:2px;background:#fff}
.nav-links{position:absolute;left:432px;top:20px;display:flex;gap:28px;font-size:16px;color:#fff;font-weight:500}
.btn-advert{position:absolute;left:867px;top:14px;width:170px;height:36px;border-radius:18px;background:var(--green);color:#fff;font-size:18px;font-weight:500;display:flex;align-items:center;justify-content:center}

/* hero */
.hero{position:absolute;left:0;top:60px;width:1200px;height:519px;overflow:hidden;
  background:
    radial-gradient(ellipse 260px 200px at 1120px 90px, rgba(205,210,200,.85), rgba(205,210,200,0) 70%),
    radial-gradient(ellipse 300px 160px at 1080px 230px, rgba(70,92,52,.9), rgba(70,92,52,0) 75%),
    radial-gradient(ellipse 120px 200px at 800px 170px, rgba(48,34,22,.9), rgba(48,34,22,0) 75%),
    radial-gradient(ellipse 420px 90px at 900px 330px, rgba(226,218,198,.75), rgba(226,218,198,0) 75%),
    radial-gradient(ellipse 160px 120px at 700px 420px, rgba(228,222,208,.7), rgba(228,222,208,0) 75%),
    radial-gradient(ellipse 600px 200px at 860px 470px, rgba(150,140,70,.95), rgba(150,140,70,0) 80%),
    radial-gradient(ellipse 300px 160px at 620px 130px, rgba(120,125,100,.6), rgba(120,125,100,0) 75%),
    linear-gradient(90deg,#1c2312 0%,#27301a 32%,#4e5134 52%,#7d7a55 70%,#8b8a68 100%)}
.brand{position:absolute;left:160px;top:52px;display:flex;align-items:center;gap:14px}
.brand-dot{width:62px;height:62px;border-radius:50%;background:var(--green)}
.brand-name{font-size:40px;font-weight:500;color:var(--gold);white-space:nowrap}
.hero h1{position:absolute;left:155px;top:250px;font-size:46px;line-height:58px;font-weight:700;color:#fff}

/* search */
.finder{position:absolute;left:0;top:579px;width:1200px;height:138px;background:#fff;border-bottom:2px solid #ddd}
.finder h2{position:absolute;left:231px;top:50px;font-size:33px;font-weight:500;color:var(--green)}
.select{position:absolute;left:521px;top:45px;width:299px;height:46px;border:1px solid #bbb;border-radius:23px;font-size:18px;padding:13px 0 0 28px;color:#444}
.select::after{content:"";position:absolute;right:48px;top:0;width:1px;height:44px;background:#bbb}
.select svg{position:absolute;right:16px;top:16px}
.btn-search{position:absolute;left:837px;top:45px;width:126px;height:44px;border-radius:22px;background:var(--green);color:#fff;font-size:22px;font-weight:500;display:flex;align-items:center;justify-content:center}

/* breeds */
.breeds{position:absolute;left:0;top:717px;width:1200px;height:306px;background:var(--grey-band)}
.breed{position:absolute;top:60px;width:150px;text-align:center;font-size:14px;line-height:17px;color:#333}
.breed .photo{display:block;width:132px;height:132px;margin:0 auto 26px;border-radius:50%;border:3px solid #fff;background-color:#f4f1ec}
.photo-lab{background:radial-gradient(ellipse 50px 45px at 50% 45%,#e9cf9e,rgba(233,207,158,0) 100%),radial-gradient(ellipse 70px 60px at 50% 75%,#d9b57a,rgba(217,181,122,0) 100%),radial-gradient(circle at 50% 50%,#f2ede4 40%,#f4f1ec 70%)}
.photo-springer{background:radial-gradient(ellipse 22px 38px at 25% 50%,#5a3424,rgba(90,52,36,0) 100%),radial-gradient(ellipse 22px 38px at 75% 50%,#5a3424,rgba(90,52,36,0) 100%),radial-gradient(ellipse 40px 50px at 50% 55%,#ddd6cc,rgba(221,214,204,0) 100%),radial-gradient(circle,#8a6a58,#f4f1ec 75%)}
.photo-cocker{background:radial-gradient(ellipse 28px 46px at 28% 55%,#b0652c,rgba(176,101,44,0) 100%),radial-gradient(ellipse 28px 46px at 72% 55%,#b0652c,rgba(176,101,44,0) 100%),radial-gradient(ellipse 40px 48px at 50% 45%,#d4914f,rgba(212,145,79,0) 100%),radial-gradient(circle,#c27a3e,#f4f1ec 78%)}
.photo-vizsla{background:radial-gradient(ellipse 45px 50px at 50% 45%,#b8643a,rgba(184,100,58,0) 100%),radial-gradient(ellipse 60px 40px at 50% 85%,#9a4e2c,rgba(154,78,44,0) 100%),radial-gradient(circle,#a85a34,#f4f1ec 80%)}
.photo-setter{background:radial-gradient(ellipse 36px 46px at 50% 45%,#6b5644,rgba(107,86,68,0) 100%),radial-gradient(ellipse 60px 40px at 50% 85%,#c9bfb2,rgba(201,191,178,0) 100%),radial-gradient(circle,#9b8a78,#f4f1ec 80%)}
.photo-pointer{background:radial-gradient(ellipse 40px 46px at 50% 42%,#5a3a2a,rgba(90,58,42,0) 100%),radial-gradient(ellipse 55px 40px at 50% 85%,#a89a90,rgba(168,154,144,0) 100%),radial-gradient(circle,#7a5c4c,#f4f1ec 80%)}

/* ads */
.ad-card{position:absolute;top:1122px;width:280px;height:432px;border:2px solid var(--gold);border-radius:10px;overflow:hidden;background:#fff;text-align:center}
.ad-card .photo{height:185px;border-bottom:8px solid var(--gold);
  background:
    radial-gradient(ellipse 34px 60px at 95px 110px,#5a2e1e,rgba(90,46,30,0) 100%),
    radial-gradient(ellipse 34px 60px at 185px 110px,#5a2e1e,rgba(90,46,30,0) 100%),
    radial-gradient(ellipse 40px 50px at 140px 85px,#6b3a26,rgba(107,58,38,0) 100%),
    radial-gradient(ellipse 36px 40px at 140px 160px,#e8e2d8,rgba(232,226,216,0) 100%),
    radial-gradient(ellipse 80px 90px at 140px 110px,#7a4a32,rgba(122,74,50,0) 100%),
    linear-gradient(180deg,#6f7d55 0%,#8a8464 45%,#9a7a5e 100%)}
.ad-card .loc{margin-top:22px;font-size:18px;font-weight:500;color:#333}
.ad-card p{margin-top:20px;font-size:18px;color:#444}
.ad-card .btn-more{display:inline-flex;margin-top:24px;width:132px;height:44px;border-radius:22px;background:var(--green);color:#fff;font-size:14px;font-weight:500;align-items:center;justify-content:center}

/* partner banner */
.partner{position:absolute;left:157px;width:883px;height:172px;background:var(--panel);display:flex;align-items:center;justify-content:center}
.partner-name{font-size:58px;font-weight:500;letter-spacing:6px;color:#555;text-align:center;line-height:62px}

/* content */
.section-title{position:absolute;left:156px;font-size:29px;font-weight:500;color:var(--green)}
.rule{position:absolute;left:156px;width:208px;height:4px;background:var(--gold)}
.thumb{position:absolute;left:156px;width:208px;height:190px;
  background:
    radial-gradient(ellipse 60px 40px at 110px 100px,#b8642a,rgba(184,100,42,0) 100%),
    radial-gradient(ellipse 40px 36px at 120px 55px,#1e1e16,rgba(30,30,22,0) 100%),
    radial-gradient(ellipse 50px 30px at 60px 120px,#8a3a22,rgba(138,58,34,0) 100%),
    radial-gradient(ellipse 120px 50px at 104px 175px,#7a8a34,rgba(122,138,52,0) 100%),
    linear-gradient(180deg,#3c4a22 0%,#5e6e2e 60%,#7f8c3a 100%)}
.copy{position:absolute;left:397px;width:362px;font-size:13.6px;line-height:18px;color:#333}
.copy p+p{margin-top:18px}
.video{position:absolute;left:156px;top:2312px;width:208px;height:189px;background:var(--green)}
.video svg{position:absolute;left:62px;top:52px}

/* sidebar */
.side-ad{position:absolute;left:833px;width:205px;height:203px;border-radius:14px;background:#fff;box-shadow:0 0 6px rgba(0,0,0,.3);text-align:center}
.side-ad .mark{display:block;width:44px;height:44px;margin:50px auto 14px;background:#1d1d1d;border-radius:4px}
.side-ad b{display:block;font-size:15px;font-weight:700;color:var(--green)}
.side-ad small{display:block;margin-top:4px;font-size:7.5px;color:#6d8a48}

/* contact */
.contact{position:absolute;left:0;top:3171px;width:1200px;height:606px;background:var(--green)}
.contact h2{position:absolute;left:0;width:1200px;top:82px;text-align:center;font-size:29px;font-weight:500;color:#fff}
.field{position:absolute;left:309px;width:581px;height:46px;border:2px solid var(--gold);border-radius:6px;color:var(--gold);font-size:14px;padding:13px 0 0 16px}
.contact-mail{position:absolute;left:309px;top:531px;display:flex;align-items:center;gap:14px;color:var(--gold);font-size:18px}
.circle-gold{width:40px;height:40px;border-radius:50%;background:var(--gold);display:flex;align-items:center;justify-content:center}
.socials{position:absolute;display:flex;gap:14px}

/* footer */
.footer{position:absolute;left:0;top:3989px;width:1200px;height:216px;background:var(--gold)}
.footer .brand{left:157px;top:70px}
.footer .brand-dot{background:var(--green)}
.footer .brand-name{color:var(--green);font-size:34px}
.foot-links{position:absolute;left:611px;top:69px;list-style:none;font-size:16px;line-height:28px;color:var(--green)}
.footer .socials{left:890px;top:67px}
.footer .socials span{width:42px;height:42px;border-radius:50%;background:var(--green)}
.legal{position:absolute;left:0;top:4205px;width:1200px;height:59px;background:#fafafa;font-size:16px;color:var(--green)}
.legal .copy-note{position:absolute;left:157px;top:21px}
.legal .policy{position:absolute;right:162px;top:21px}
</style>
</head>
<body>

<header class="topbar">
  <div class="menu-btn"><i style="top:6px"></i><i style="top:11px"></i><i style="top:16px"></i></div>
  <nav class="nav-links"><span>Lost / Stolen Dogs</span><span>Events</span><span>Information</span></nav>
  <div class="btn-advert">PLACE ADVERT</div>
</header>

<section class="hero" role="img" aria-label="Huntsman on horseback with a pack of hounds running across a field toward the viewer">
  <div class="brand"><span class="brand-dot"></span><span class="brand-name">FieldHound Market</span></div>
  <h1>FIND YOUR PERFECT<br>GUNDOG TODAY</h1>
</section>

<section class="finder">
  <h2>FIND A GUNDOG</h2>
  <div class="select">Select County
    <svg width="14" height="12" viewBox="0 0 14 12"><path d="M0 0h14L7 12z" fill="#555"/></svg>
  </div>
  <div class="btn-search">SEARCH</div>
</section>

<section class="breeds">
  <div class="breed" style="left:144px"><span class="photo photo-lab" role="img" aria-label="Labrador portrait"></span>LABRADORS</div>
  <div class="breed" style="left:294px"><span class="photo photo-springer" role="img" aria-label="Springer spaniel portrait"></span>SPRINGER<br>SPANIELS</div>
  <div class="breed" style="left:447px"><span class="photo photo-cocker" role="img" aria-label="Cocker spaniel portrait"></span>COCKER<br>SPANIELS</div>
  <div class="breed" style="left:598px"><span class="photo photo-vizsla" role="img" aria-label="Hungarian Vizsla portrait"></span>HUNGARIAN<br>VISLA</div>
  <div class="breed" style="left:750px"><span class="photo photo-setter" role="img" aria-label="English setter portrait"></span>ENGLISH<br>SETTER</div>
  <div class="breed" style="left:898px"><span class="photo photo-pointer" role="img" aria-label="Pointer portrait"></span>POINTER</div>
</section>

<article class="ad-card" style="left:158px"><div class="photo" role="img" aria-label="Springer spaniel for sale"></div><div class="loc">Kinross , Kinross</div><p>6th October 2023</p><p>£2000.00</p><span class="btn-more">VIEW MORE</span></article>
<article class="ad-card" style="left:459px"><div class="photo" role="img" aria-label="Springer spaniel for sale"></div><div class="loc">Kinross , Kinross</div><p>6th October 2023</p><p>£2000.00</p><span class="btn-more">VIEW MORE</span></article>
<article class="ad-card" style="left:758px"><div class="photo" role="img" aria-label="Springer spaniel for sale"></div><div class="loc">Kinross , Kinross</div><p>6th October 2023</p><p>£2000.00</p><span class="btn-more">VIEW MORE</span></article>

<div class="partner" style="top:1599px"><span class="partner-name">ASHMERE<br>GUNDOGS</span></div>

<h2 class="section-title" style="top:1828px">Welcome To FieldHound Market</h2>
<div class="rule" style="top:1879px"></div>
<div class="thumb" style="top:1907px" role="img" aria-label="Gundog retrieving a pheasant"></div>
<div class="copy" style="top:1903px">
  <p>Our aim at FieldHound Market has always been to provide the very best gundog advertisement platform to purchase and sell your gundogs in the safest possible way. FieldHound Market was created by gundog people that know your time is valuable and best spent in the field with your dogs, thats why we have no lengthy registration forms to fill in or no accounts to remember passwords for adverts you posted 3 months ago.</p>
  <p>Here at FieldHound Market your advert stays on until sold and all we ask in return is that you keep your advert updated with our email edit links so our customers looking to purchase their new gun dog can make the best informed decisions.</p>
</div>

<h2 class="section-title" style="top:2217px">FieldHound Market Safe Deposit Service</h2>
<div class="rule" style="top:2271px"></div>
<div class="video" role="img" aria-label="Video about the safe deposit service">
  <svg width="86" height="86" viewBox="0 0 86 86"><circle cx="43" cy="43" r="39" fill="none" stroke="#d6a45a" stroke-width="6"/><path d="M34 28l24 15-24 15z" fill="#d6a45a"/></svg>
</div>
<div class="copy" style="top:2309px">
  <p>Your safety is our number one priority when purchasing a gun dog and we have teamed up with SafeHold who have tailor made a gundog escrow just for YOU, so now you can pay deposits for gun dogs safely without the fear of being scammed and losing deposits for your new gun dog. We have made the FieldHound Market Safe Deposit Service FREE for all breeders to use so there is really no good reason not to support the service and help keep the buyers safe when they part with large sums of money.</p>
  <p>To know more about the FieldHound Market Safe Deposit Service and how it works please watch this video https://www.clipstream.co.uk/watch?v=aB3dK9xQ</p>
</div>

<h2 class="section-title" style="top:2624px">Buy, Sell &amp; Connect</h2>
<div class="rule" style="top:2678px"></div>
<div class="thumb" style="top:2719px" role="img" aria-label="Gundog retrieving a pheasant"></div>
<div class="copy" style="top:2715px">
  <p>When you post an advert with FieldHound Market you will be sent a email confirmation (check spam folder) on that email you will find an edit link that allows you to edit your gundog advert when you like, we advice you keep the email safe for future use. If you post an advert we ask that you keep them up to date at all times. When you sell your gundog you can edit your own advert and mark the dog has sold. If the advert is left for over 3 months without any edits we will automatically delete the advert, this is to stop old adverts blocking up the site.</p>
  <p>We are here to serve the gun dog community and to do that we have set up Stolen Dogs and Events &amp; Trails category's which is FREE to advertise. We want our customers to work with us to eliminate stolen working dogs and connect through gun dog events up and down the UK. FieldHound Market is passionate about all things gundogs and we know you are too. Should you need any further assistance please email info@fieldhoundmarket.co.uk</p>
</div>

<aside>
  <div class="side-ad" style="top:1837px"><span class="mark"></span><b>Ridgeway Dog Training</b><small>Training for dogs and their owners too.</small></div>
  <div class="side-ad" style="top:2071px"><span class="mark"></span><b>Ridgeway Dog Training</b><small>Training for dogs and their owners too.</small></div>
  <div class="side-ad" style="top:2309px"><span class="mark"></span><b>Ridgeway Dog Training</b><small>Training for dogs and their owners too.</small></div>
  <div class="side-ad" style="top:2548px"><span class="mark"></span><b>Ridgeway Dog Training</b><small>Training for dogs and their owners too.</small></div>
  <div class="side-ad" style="top:2789px"><span class="mark"></span><b>Ridgeway Dog Training</b><small>Training for dogs and their owners too.</small></div>
</aside>

<section class="contact">
  <h2>Get In Touch</h2>
  <div class="field" style="top:141px">Name</div>
  <div class="field" style="top:202px">Phone</div>
  <div class="field" style="top:265px">Email</div>
  <div class="field" style="top:333px;height:139px">Message</div>
  <div class="contact-mail">
    <span class="circle-gold"><svg width="20" height="14" viewBox="0 0 20 14"><rect x="1" y="1" width="18" height="12" rx="1" fill="none" stroke="#4f6135" stroke-width="2"/><path d="M1 1l9 7 9-7" fill="none" stroke="#4f6135" stroke-width="2"/></svg></span>
    info@fieldhoundmarket.co.uk
  </div>
  <div class="socials" style="left:800px;top:531px"><span class="circle-gold"></span><span class="circle-gold"></span></div>
</section>

<div class="partner" style="top:3798px"><span class="partner-name">ASHMERE<br>GUNDOGS</span></div>

<footer class="footer">
  <div class="brand"><span class="brand-dot"></span><span class="brand-name">FieldHound Market</span></div>
  <ul class="foot-links"><li>Home</li><li>Information</li><li>Buyer Deposit Service</li><li>Contact Us</li></ul>
  <div class="socials"><span></span><span></span></div>
</footer>
<div class="legal">
  <span class="copy-note">© Copyright FieldHound Market 2023.</span>
  <span class="policy">Terms &amp; Conditions &nbsp;|&nbsp; Privacy Policy</span>
</div>

</body>
</html>
```